Beauty care products face masks Layout

--- English below --- We need a label set (2 pieces á 35x80mm) for a black 50ml tube. The logo and the subtitles are displayed in the Annexes. A black drop should be incorporated into the label. Brand Name: lumaV Product name: sable subtitles: Deep cleansing peel-off mask required entry is: 50 ml / 1.69 fl.oz. On the back: Recommended use: In order to achieve the best results for you, we recommend that you clean your face thoroughly and dry. Apply the mask, thereby avoiding the mouth and eye area. After 20-30 minutes the mask is dried and can be pulled off. Purify by removing the mask, your face with warm water. We recommend a calming face cream after the application to use. The mask Please do not dispose of in the toilet. Application: Every 2-3 days Ingredients (ingredients): Water, Polyvinyl Alcohol, Glycerin, Citrus Paradisi, PEG-8, panthenol, Fragrance, Cellulose Gum, tetra sodium EDTA, Activated carbon, Rosemary Extract, Avena sativa Extract, Pot Marigold , Zinc Gluconate, lecithin, Retinyl Palmitate, arachidyl propionate, tocopheryl acetate, ethyl Liloenate, xanthan Gum, Limonene, linalool, geraniol, methyl paraben English: We need a label set (2 pieces 35mm wide 80mm height) for a black 50ml tube. You can find the logo as well as the subtitel in the attachments. Brand Name: lumaV Product Name: sable Subtitle: Deep cleansing peel-off mask On the back label: Recommended use: In order to achieve the best results for you, we recommend that you clean your face thoroughly and dry. Apply the mask, thereby avoiding the mouth and eye area. After 20-30 minutes the mask is dried and can be pulled off. Purify by removing the mask, your face with warm water. We recommend a calming face cream after the application to use. The mask Please do not dispose of in the toilet. Application: Every 2-3 days Ingredients (ingredients): Water, Polyvinyl Alcohol, Glycerin, Citrus Paradisi, PEG-8, panthenol, Fragrance, Cellulose Gum, tetra sodium EDTA, Activated carbon, Rosemary Extract, Avena sativa Extract, Pot Marigold , Zinc Gluconate, lecithin, Retinyl Palmitate, arachidyl propionate, tocopheryl acetate, ethyl Liloenate, xanthan Gum, Limonene, linalool, geraniol, methyl paraben

Target Market(s)

Cosmetics, Beauty, Body Care, Women

Requirements
Must have
• Clear lines to possibly expanding the range Clear design for possible other products
Nice to have
• The design should be more female. We prefer a feminine design.

```html
<!DOCTYPE html>
<html lang="en">
<head>
<meta charset="utf-8">
<title>LUMAV sable – label set</title>
<link rel="stylesheet" href="https://fonts.googleapis.com/css2?family=Jost:ital,wght@0,400;0,500;1,400;1,500&display=swap">
<style>
  :root {
    --bg: #d4d4d4;
    --frame: #ffffff;
    --panel-side: #9b52a5;
    --panel-side-light: #a862b1;
    --panel-front: #bb4fc6;
    --panel-front-light: #cb6ad4;
    --ink: #2b0f31;
    --on-front: #ffffff;
    --rule: #c9c9c9;
  }
  html, body {
    margin: 0;
    padding: 0;
    width: 1200px;
    height: 1200px;
    overflow: hidden;
    background: var(--bg);
  }
  .canvas {
    position: relative;
    width: 1200px;
    height: 1200px;
    font-family: "Jost", sans-serif;
  }
  .label-set {
    position: absolute;
    left: 144px;
    top: 458px;
    width: 894px;
    height: 330px;
    border: 5px solid var(--frame);
    display: grid;
    grid-template-columns: 284px 352px 258px;
    background: linear-gradient(135deg, var(--panel-side-light), var(--panel-side) 60%, var(--panel-side-light));
  }
  .panel {
    box-sizing: border-box;
    color: var(--ink);
    text-align: center;
    font-style: italic;
  }
  .panel-heading {
    margin: 0 0 4px;
    font-size: 15px;
    font-weight: 400;
    letter-spacing: 0.2px;
  }
  .panel-body {
    margin: 0;
    font-size: 11.5px;
    line-height: 21.8px;
  }
  .panel-ingredients { padding: 58px 50px 0 34px; }
  .panel-application { padding: 62px 30px 0 28px; }
  .panel-application .panel-body { line-height: 20.2px; }
  .panel-front {
    position: relative;
    background: linear-gradient(120deg, var(--panel-front), var(--panel-front-light) 55%, var(--panel-front));
    border-top: 3px solid var(--rule);
    border-bottom: 3px solid var(--rule);
    font-style: normal;
  }
  .brand-name {
    position: absolute;
    top: 20px;
    width: 100%;
    margin: 0;
    font-size: 28px;
    font-weight: 400;
    letter-spacing: 4px;
    line-height: 1.2;
    color: var(--ink);
  }
  .product-name {
    position: absolute;
    top: 116px;
    width: 100%;
    margin: 0;
    font-size: 66px;
    font-weight: 400;
    letter-spacing: 10px;
    line-height: 1;
    text-transform: uppercase;
    color: var(--on-front);
  }
  .product-subtitle {
    position: absolute;
    top: 214px;
    width: 100%;
    margin: 0;
    font-size: 12px;
    color: var(--on-front);
  }
  .producer {
    position: absolute;
    top: 284px;
    width: 100%;
    margin: 0;
    font-size: 12px;
    color: var(--ink);
  }
</style>
</head>
<body>
<main class="canvas">
  <section class="label-set">
    <div class="panel panel-ingredients">
      <h2 class="panel-heading">INGREDIENTS:</h2>
      <p class="panel-body">Water, polyvinyl alcohol, glycerin, Citrus Paradisi, PEG-8, panthenol, Fragrance, cellulose gum, tetra- Sodium EDTA, activated carbon, Rosemary Extract, Avena sativa Extract, Pot Marigold, Zinc Gluconates, lecithin, retinyl Palmitates, arachidyl propionates, Tocopheryl acetates, ethyl liloenates, Xanthan gum, limonene, linalool, Geraniol, methylparaben</p>
    </div>
    <div class="panel panel-front">
      <p class="brand-name">LUMAV</p>
      <h1 class="product-name">sable</h1>
      <p class="product-subtitle">Tiefenreinigende peel-off Maske</p>
      <p class="producer">by Velora | Leiden</p>
    </div>
    <div class="panel panel-application">
      <h2 class="panel-heading">APPLICATION:</h2>
      <p class="panel-body">For the best result for you, please clean your face thoroughly and dry.<br>Then apply the mask while avoiding mouth and eye area.<br>After 20-30 minutes, the mask is dried and can be peeled off.<br>After removing the mask, rinse the face with warm water.<br>Do not dispose of the mask in the toilet.</p>
    </div>
  </section>
</main>
</body>
</html>
```